Business Card Design For Tidecrest Audio

Tidecrest Audio is a small pro-audio company providing rental and install services for professional sound reinforcement. Focus is gigs (any gigs) needing high quality audio; from corporate to chamber music to hard hitting rock.

Tidecrest Audio
Live sound for every stage ... chills included
Doran Pelley
doran@tidecrestaudio.example.com.au
0482 356 071

We need a business card design and an "drop-off"' larger card (eg. one third A4 size: 99mm wide x 210mm high) with more details.
Updates

Please note I've had limited internet access for last few days and for the next four.  The work so far looks great .. I'll provide some individual feedback on the designs now.  Great work, many thanks, love the creativity!

Doran

Industry/Entity Type

Business

```html
<!DOCTYPE html>
<html lang="en">
<head>
<meta charset="utf-8">
<title>Tidecrest Audio — Business Card</title>
<link rel="stylesheet" href="https://fonts.googleapis.com/css2?family=Orbitron:wght@900&family=Russo+One&family=Delius&family=Abel&display=swap">
<style>
  :root {
    --card-black: #000000;
    --title-white: #ffffff;
    --ink-dark: #1e1e1e;
    --panel-light: #ededed;
    --panel-mid: #a9a9a9;
    --panel-dark: #4a4a4a;
    --art-grey: #5e5e5e;
    --art-shadow: #2a2a2a;
  }
  * { margin: 0; padding: 0; box-sizing: border-box; }
  html, body {
    width: 1200px;
    height: 566px;
    overflow: hidden;
    background: var(--card-black);
  }
  .card {
    position: relative;
    width: 1200px;
    height: 566px;
    background: var(--card-black);
    overflow: hidden;
  }
  .card__shapes {
    position: absolute;
    inset: 0;
    width: 1200px;
    height: 566px;
  }
  .card__headphone-art {
    position: absolute;
    left: 840px;
    top: 20px;
    width: 330px;
    height: 546px;
    border-radius: 150px 150px 40px 40px;
    background: radial-gradient(ellipse at 55% 65%, var(--art-grey) 0%, var(--art-shadow) 60%, rgba(0,0,0,0) 78%);
    opacity: 0.9;
  }
  .card__brand {
    position: absolute;
    left: 0;
    top: 117px;
    width: 1200px;
    padding-left: 20px;
    text-align: center;
    font-family: "Orbitron", sans-serif;
    font-weight: 900;
    font-size: 80px;
    line-height: 1;
    letter-spacing: 1px;
    color: var(--title-white);
    text-transform: uppercase;
    white-space: nowrap;
  }
  .card__tagline {
    position: absolute;
    left: 0;
    top: 244px;
    width: 1200px;
    text-align: center;
    font-family: "Russo One", sans-serif;
    font-style: italic;
    font-size: 21px;
    line-height: 1;
    letter-spacing: 1px;
    color: var(--title-white);
    text-transform: uppercase;
    white-space: nowrap;
  }
  .card__name {
    position: absolute;
    left: 66px;
    top: 366px;
    font-family: "Delius", cursive;
    font-weight: 400;
    font-size: 60px;
    line-height: 1;
    color: var(--ink-dark);
    white-space: nowrap;
  }
  .card__contact {
    position: absolute;
    left: 72px;
    top: 458px;
    font-family: "Abel", sans-serif;
    font-size: 27px;
    line-height: 41px;
    color: var(--ink-dark);
    list-style: none;
    white-space: nowrap;
  }
</style>
</head>
<body>
  <main class="card">
    <svg class="card__shapes" viewBox="0 0 1200 566" aria-hidden="true">
      <defs>
        <linearGradient id="contactPanelFill" x1="0" y1="0" x2="1" y2="0">
          <stop offset="0" stop-color="var(--panel-light)"/>
          <stop offset="0.45" stop-color="var(--panel-mid)"/>
          <stop offset="1" stop-color="var(--panel-dark)"/>
        </linearGradient>
      </defs>
      <polygon class="card__contact-panel" points="0,330 575,330 830,566 0,566" fill="url(#contactPanelFill)"/>
    </svg>

    <div class="card__headphone-art" role="img" aria-label="Grunge-style illustration of studio headphones with a trailing audio cable and jack plugs"></div>

    <h1 class="card__brand">Tidecrest Audio</h1>
    <p class="card__tagline">Live sound for every stage ... chills included</p>

    <h2 class="card__name">Doran Pelley</h2>
    <ul class="card__contact">
      <li class="card__email">E. doran@tidecrestaudio.example.com.au</li>
      <li class="card__phone">P. 0482 356 071</li>
    </ul>
  </main>
</body>
</html>
```